Orbe Trophy Banner 3 Feet by 8 Feet

It seems like the photos i submitted are bad quality. Feel free to find some of your own with better resolution. I am not super picky on what is uses as I think I've conveyed my concept and most of you understand.
FEEL FREE TO GET CREATIVE AND ADD PICS OF UR OWN IF U WANT
I am going to Brazil for orbe trophy as a Fan of Solvantia Futbol Squad. I need a super bad ass banner design. I am not picky and I am attaching several images that you are free to play with. Requirements are as follow:
1. The two pictures of the saints would be ideal. Blend them in so they dont look like like square images.
2. On the bottom at smaller scale so it doesnt take much space. the pixaro sign with our pixaro user names. so pixaro logo and next to it. @rivotalsen82 @kortuvex519 then the following hashtags: #dalubreno #pelotirunacasoba #guardianesdelmaizdorado #torvela2014
3. If you can add the Teleandra Logo (which is a channel logo) somewhere so it grabs attention from media it would be cool. Not mandatory.
4. Logo of mexican national team (this can take a lot of space)
5. Lastly the main text or content which would take most of the space, 'Vamos México, vamos Selección! Contigo siempre de corazón!
IF YOU ARE ABLE TO USE MOST PICTURES AND MAKE IT LOOK NICE AND THAT IT FLOWS YOULL MAKE MY LIFE.
Updates
i made a small change with main text. I really like the mexican national logo as back ground even if i have to lose out on the crappy pixilated images. LIke I've said before u can find better images online. pixaro logo on bottom is important with first user names @rivotalsen82 @kortuvex519 followed by all the hashtags
Sorry guys i screwed up the size is not 8 by 10 but 3 feet by 8 feet! I am sorry, I will add additional prize amount for the troubles! I will add additional $30 dollars

```html
<!DOCTYPE html>
<html lang="es">
<head>
<meta charset="utf-8">
<title>Solvantia Futbol Squad – Orbe Trophy Banner</title>
<link rel="stylesheet" href="https://fonts.googleapis.com/css2?family=Anton&family=Russo+One&display=swap">
<style>
  :root {
    --page: #ffffff;
    --banner: #000000;
    --green-light: #5cf08e;
    --green-dark: #0c9a48;
    --silver-light: #ffffff;
    --silver-dark: #9a9a9a;
    --red-light: #ff4a32;
    --red-dark: #a8000c;
    --gold: #c6a56a;
    --white: #ffffff;
    --label: #d9d9d9;
  }
  html, body {
    margin: 0;
    padding: 0;
    width: 1200px;
    height: 1000px;
    overflow: hidden;
    background: var(--page);
  }
  .banner {
    position: absolute;
    left: 16px;
    top: 294px;
    width: 1168px;
    height: 437px;
    background: var(--banner);
  }
  .banner svg { display: block; }
  .headline { font-family: "Anton", "Impact", sans-serif; }
  .handles { font-family: "Russo One", "Arial Black", sans-serif; }
  .brand-name { font-family: "Anton", "Impact", sans-serif; fill: var(--white); }
</style>
</head>
<body>
<div class="banner">
  <svg width="1168" height="437" viewBox="0 0 1168 437" xmlns="http://www.w3.org/2000/svg">
    <defs>
      <linearGradient id="green-fill" x1="0" y1="0" x2="0" y2="1">
        <stop offset="0" stop-color="var(--green-light)"/>
        <stop offset="1" stop-color="var(--green-dark)"/>
      </linearGradient>
      <linearGradient id="silver-fill" x1="0" y1="0" x2="0" y2="1">
        <stop offset="0" stop-color="var(--silver-light)"/>
        <stop offset="0.55" stop-color="#d0d0d0"/>
        <stop offset="1" stop-color="var(--silver-dark)"/>
      </linearGradient>
      <linearGradient id="red-fill" x1="0" y1="0" x2="0" y2="1">
        <stop offset="0" stop-color="var(--red-light)"/>
        <stop offset="1" stop-color="var(--red-dark)"/>
      </linearGradient>
      <radialGradient id="player-left-fill" cx="0.5" cy="0.55" r="0.55">
        <stop offset="0" stop-color="#2f6a48"/>
        <stop offset="0.6" stop-color="#163a28"/>
        <stop offset="1" stop-color="#000000" stop-opacity="0"/>
      </radialGradient>
      <radialGradient id="player-right-fill" cx="0.55" cy="0.5" r="0.55">
        <stop offset="0" stop-color="#336e4c"/>
        <stop offset="0.6" stop-color="#173c2a"/>
        <stop offset="1" stop-color="#000000" stop-opacity="0"/>
      </radialGradient>
      <radialGradient id="flare" cx="0.5" cy="0.5" r="0.5">
        <stop offset="0" stop-color="#ffffff" stop-opacity="0.9"/>
        <stop offset="1" stop-color="#ffffff" stop-opacity="0"/>
      </radialGradient>
    </defs>

    <!-- players -->
    <rect class="player-photo" x="74" y="66" width="420" height="330" fill="url(#player-left-fill)"
          role="img" aria-label="Photo of a Solvantia player in a green jersey shouting in celebration with fists clenched"/>
    <rect class="player-photo" x="540" y="4" width="628" height="390" fill="url(#player-right-fill)"
          role="img" aria-label="Photo of a Solvantia player in a green jersey celebrating with arms spread wide"/>

    <!-- channel marks -->
    <g class="channel-mark">
      <rect x="38" y="26" width="32" height="32" fill="var(--label)"/>
      <text class="brand-name" x="54" y="96" font-size="15" text-anchor="middle">TELEANDRA</text>
    </g>
    <g class="channel-mark">
      <rect x="1097" y="26" width="32" height="32" fill="var(--label)"/>
      <text class="brand-name" x="1113" y="96" font-size="15" text-anchor="middle">TELEANDRA</text>
    </g>

    <!-- team mark -->
    <g class="team-mark">
      <circle cx="584" cy="164" r="104" fill="none" stroke="var(--gold)" stroke-width="4"/>
      <text class="brand-name" x="584" y="160" font-size="30" text-anchor="middle">SOLVANTIA</text>
      <text class="brand-name" x="584" y="192" font-size="18" text-anchor="middle">FUTBOL SQUAD</text>
      <ellipse cx="584" cy="280" rx="70" ry="14" fill="url(#flare)"/>
    </g>

    <!-- headlines -->
    <text class="headline" x="117" y="80" font-size="58" textLength="355" lengthAdjust="spacingAndGlyphs"
          fill="url(#green-fill)">VAMOS MÉXICO</text>
    <text class="headline" x="682" y="80" font-size="58" textLength="364" lengthAdjust="spacingAndGlyphs"
          fill="url(#silver-fill)">VAMOS SELECCIÓN!</text>
    <text class="headline" x="24" y="366" font-size="102" textLength="1120" lengthAdjust="spacingAndGlyphs"
          fill="url(#red-fill)" stroke="#3a0000" stroke-width="1.5">CONTIGO SIEMPRE DE CORAZÓN!</text>

    <!-- social row -->
    <g class="social-mark">
      <rect x="36" y="378" width="16" height="16" fill="var(--label)"/>
      <text class="brand-name" x="44" y="412" font-size="11" text-anchor="middle">PIXARO</text>
    </g>
    <g class="social-mark">
      <rect x="1116" y="378" width="16" height="16" fill="var(--label)"/>
      <text class="brand-name" x="1124" y="412" font-size="11" text-anchor="middle">PIXARO</text>
    </g>
    <text class="handles" x="74" y="403" font-size="16" fill="var(--white)" textLength="1018" lengthAdjust="spacing"
          xml:space="preserve">@RIVOTALSEN82   @KORTUVEX519   #DALUBRENO   #PELOTIRUNACASOBA   #GUARDIANESDELMAIZDORADO   #TORVELA2014</text>
  </svg>
</div>
</body>
</html>
```